Business card required for IT Consultancy Business - Tealbrook Consulting.
Company provides the whole nine yards of services across IT Architecture, design and execution.
Basically we provide consulting services to help businesses make sure their technology is enabling their business strategy.
Design for front and back required.
We would like the front of the card to inlcude:
Name
Title
Mobile number
email address
www.tbkc.com.au
Company logos attached.
Thank you
Industry/Entity Type
Business
Contact Information for Business Card
Name
Title
Mobile number
email address
www.tbkc.com.au
Look and feel
Each slider illustrates characteristics of the customer's brand and the style your logo design should communicate.

```html
<!DOCTYPE html>
<html lang="en">
<head>
<meta charset="utf-8">
<title>Tealbrook Consulting – Business Card</title>
<link rel="stylesheet" href="https://fonts.googleapis.com/css2?family=Montserrat:wght@400;600;700&family=Arimo:wght@400;700&display=swap">
<style>
  :root {
    --page-bg: #e6e7e9;
    --card-white: #ffffff;
    --brand-orange: #d9552a;
    --brand-blue: #1f72b8;
    --ink-dark: #2b2b2b;
    --ink-white: #ffffff;
  }
  * { margin: 0; padding: 0; box-sizing: border-box; }
  html, body {
    width: 1200px; height: 997px; overflow: hidden;
    background: var(--page-bg);
    font-family: "Arimo", Arial, sans-serif;
  }
  .stage { position: relative; width: 1200px; height: 997px; }
  .card {
    position: absolute;
    width: 560px; height: 320px;
    border-radius: 22px;
    background: var(--card-white);
    overflow: hidden;
    box-shadow: 0 10px 30px rgba(0,0,0,0.18);
  }
  .card--back { left: 70px; top: 110px; }
  .card--front { left: 570px; top: 470px; }

  /* back side */
  .back-mark {
    position: absolute; inset: 0;
    display: flex; align-items: center; justify-content: center; gap: 18px;
  }
  .back-mark__dot {
    width: 46px; height: 46px; border-radius: 50%;
    background: var(--brand-orange);
  }
  .back-mark__name {
    font-family: "Montserrat", sans-serif;
    font-weight: 700; font-size: 40px;
    color: var(--brand-blue); letter-spacing: 1px;
  }

  /* front side */
  .front-wave { position: absolute; inset: 0; }
  .front-logo {
    position: absolute; left: 150px; top: 62px;
    display: flex; align-items: center; gap: 12px;
  }
  .front-logo__dot {
    width: 34px; height: 34px; border-radius: 50%;
    background: var(--brand-orange);
  }
  .front-logo__name {
    font-family: "Montserrat", sans-serif;
    font-weight: 700; font-size: 28px;
    color: var(--brand-blue);
  }
  .person {
    position: absolute; left: 34px; top: 188px;
  }
  .person__name {
    font-weight: 700; font-size: 20px; color: var(--ink-white);
    text-transform: uppercase; letter-spacing: 0.5px;
  }
  .person__title { font-size: 14px; color: var(--ink-dark); margin-top: 2px; }
  .contact-list {
    list-style: none; position: absolute; left: 34px; top: 248px;
  }
  .contact-list li {
    display: flex; align-items: center; gap: 10px;
    font-size: 13px; color: var(--ink-white); height: 21px;
  }
  .contact-list svg { width: 15px; height: 15px; flex: none; }
  .company-address {
    position: absolute; right: 26px; top: 200px;
    text-align: right; font-size: 13px; line-height: 1.3; color: var(--ink-dark);
  }
  .company-address strong { color: var(--ink-white); font-size: 13px; }
</style>
</head>
<body>
<main class="stage">

  <section class="card card--back" aria-label="Card back">
    <div class="back-mark">
      <span class="back-mark__dot"></span>
      <span class="back-mark__name">Tealbrook</span>
    </div>
  </section>

  <section class="card card--front" aria-label="Card front">
    <svg class="front-wave" viewBox="0 0 560 320" preserveAspectRatio="none" aria-hidden="true">
      <path d="M0 150 C120 120 250 125 330 150 C420 175 500 130 560 118 L560 320 L0 320 Z" fill="var(--brand-orange)"/>
      <path d="M0 150 C110 124 200 118 290 138 C200 124 110 132 0 162 Z" fill="var(--brand-blue)"/>
      <path d="M300 142 C400 168 490 128 560 100 L560 112 C490 140 400 176 300 142 Z" fill="var(--brand-blue)"/>
    </svg>

    <div class="front-logo">
      <span class="front-logo__dot"></span>
      <span class="front-logo__name">Tealbrook Consulting</span>
    </div>

    <div class="person">
      <p class="person__name">Nora Pell</p>
      <p class="person__title">Director</p>
    </div>

    <ul class="contact-list">
      <li>
        <svg viewBox="0 0 16 16" aria-hidden="true"><circle cx="8" cy="8" r="8" fill="var(--brand-blue)"/><path d="M5 4.5h2l.6 2-1 .8a5 5 0 0 0 2.1 2.1l.8-1 2 .6v2c-4 .3-6.8-2.5-6.5-6.5z" fill="#fff"/></svg>
        +61 3 9000 1200
      </li>
      <li>
        <svg viewBox="0 0 16 16" aria-hidden="true"><circle cx="8" cy="8" r="8" fill="var(--brand-blue)"/><rect x="5.5" y="3.5" width="5" height="9" rx="1" fill="#fff"/></svg>
        +61 400 555 018
      </li>
      <li>
        <svg viewBox="0 0 16 16" aria-hidden="true"><circle cx="8" cy="8" r="8" fill="var(--brand-blue)"/><rect x="4" y="5" width="8" height="6" fill="#fff"/><path d="M4 5l4 3 4-3" stroke="var(--brand-blue)" fill="none"/></svg>
        hello@tbkc.com
      </li>
    </ul>

    <address class="company-address">
      <strong>TEALBROOK CONSULTING PVT LTD</strong><br>
      Level 3, 12 Harbour Lane<br>
      Melbourne VIC 3000 Australia
    </address>
  </section>

</main>
</body>
</html>
```